Tobin's Jewelry Studio Needs a Moving Location Flyer

We need a flyer to inform our customers of our location moving. We will be moving to our city's downtown which is only 1 mile away from our current address. We will be having a moving sale ( Up to 80% off). The sale starts Sept. 8th Our business creates, sells, and repairs fine jewelry. Dimensions are 5"x8"

Target Market(s)

Women ages 25-55

Industry/Entity Type

Jewelry

Colors
85abd2
cfdeed

Requirements
Must have
• Our logo
• Mention of the sale
• Our current address
• 4785 Cresthaven Blvd.
• Dunmore, Ca 94318
• (415)826-3319
Nice to have
• Mention that we're relocating to downtown Dunmore (new location opening Nov. 1st.)

```html
<!DOCTYPE html>
<html lang="en">
<head>
<meta charset="utf-8">
<title>Tobin's Jewelry Studio – Moving Sale Flyer</title>
<link href="https://fonts.googleapis.com/css2?family=Montserrat:wght@400;500;600;700&display=swap" rel="stylesheet">
<style>
:root{
  --brown:#4a2d28;
  --sky:#c0e4ea;
  --dot:#a9dbe3;
  --paper:#ffffff;
  --backdrop:#8a8a8a;
}
*{margin:0;padding:0;box-sizing:border-box}
html,body{width:1200px;height:1000px;overflow:hidden;background:var(--backdrop)}
.flyer{position:absolute;left:322px;top:45px;width:560px;height:897px;background:var(--paper);font-family:'Montserrat',sans-serif;color:var(--brown)}
.abs{position:absolute}
.center{left:0;width:560px;text-align:center}
.brand{top:58px;display:flex;align-items:center;justify-content:center;gap:12px}
.brand-rule{width:32px;height:3px;background:var(--brown)}
.brand-dot{width:34px;height:34px;border-radius:50%;background:var(--sky)}
.brand-name{font-size:19px;font-weight:600;color:var(--brown)}
.dot-band{background:var(--dot);height:12px;border-radius:6px}
.sky-strip{top:115px;left:0;width:560px;height:6px;background:var(--sky)}
.frame{left:8px;top:127px;width:544px;height:650px;background:var(--sky);border:3px solid var(--brown)}
.frame svg{position:absolute;left:-3px;top:-3px}
.moving{top:140px;font-size:52px;font-weight:700;line-height:1}
.sale{top:178px;font-size:130px;font-weight:700;line-height:1;letter-spacing:-2px}
.upto{left:77px;top:307px;width:22px;height:108px;background:var(--brown);color:var(--sky);font-size:16px;font-weight:700;display:flex;align-items:center;justify-content:center}
.upto span{transform:rotate(-90deg);white-space:nowrap;letter-spacing:1px}
.big-80{left:126px;top:268px;font-size:232px;font-weight:700;line-height:1;letter-spacing:-4px;-webkit-text-stroke:2px var(--brown)}
.percent{left:462px;top:302px;font-size:82px;font-weight:600;line-height:1}
.ribbon{left:43px;top:478px;width:475px;height:34px}
.ribbon-text{left:43px;top:478px;width:475px;height:34px;line-height:34px;text-align:center;color:var(--sky);font-size:15px;font-weight:500;letter-spacing:.5px}
.starts{left:136px;top:534px;font-size:22px;font-weight:500;letter-spacing:4px;line-height:1}
.date{left:134px;top:553px;font-size:74px;font-weight:700;line-height:1;letter-spacing:-1px}
.date sup{font-size:30px;position:relative;top:-34px;margin-left:4px;vertical-align:baseline}
.relocating{top:682px;font-size:20px;font-weight:500;letter-spacing:8px;line-height:1}
.downtown{top:699px;font-size:35px;font-weight:700;letter-spacing:1px;line-height:1.1}
.opening{top:739px;font-size:23px;font-weight:600;line-height:1.1}
.opening sup{font-size:12px;margin-left:4px}
.address{right:10px;top:824px;font-size:18px;font-weight:500;text-align:right}
.phone{right:10px;top:851px;font-size:24px;font-weight:700;text-align:right}
.decor{position:absolute;left:0;top:0}
</style>
</head>
<body>
<main class="flyer">
  <header class="abs center brand">
    <span class="brand-rule"></span>
    <span class="brand-dot"></span>
    <span class="brand-name">Tobin's Jewelry Studio</span>
    <span class="brand-rule"></span>
  </header>
  <div class="abs dot-band" style="left:8px;top:98px;width:106px" role="img" aria-label="Row of light blue dots"></div>
  <div class="abs dot-band" style="left:458px;top:98px;width:96px" role="img" aria-label="Row of light blue dots"></div>
  <div class="abs sky-strip"></div>

  <section class="abs frame">
    <svg width="544" height="650" viewBox="0 0 544 650">
      <polygon points="0,0 36,0 0,36" fill="var(--brown)"/>
      <polygon points="544,0 508,0 544,36" fill="var(--brown)"/>
      <polygon points="0,650 36,650 0,614" fill="var(--brown)"/>
      <polygon points="544,650 508,650 544,614" fill="var(--brown)"/>
    </svg>
  </section>

  <h1 class="abs center moving">MOVING</h1>
  <h2 class="abs center sale">SALE</h2>
  <div class="abs upto"><span>UP TO</span></div>
  <div class="abs big-80">80</div>
  <div class="abs percent">%</div>

  <svg class="abs ribbon" viewBox="0 0 475 34"><polygon points="0,0 475,0 460,17 475,34 0,34 15,17" fill="var(--brown)"/></svg>
  <p class="abs ribbon-text">WE CREATES, SELLS, AND REPAIRS FINE JEWELRY</p>

  <p class="abs starts">STARTS FROM</p>
  <p class="abs date">SEPT.8<sup>TH</sup></p>

  <svg class="decor" width="560" height="897" viewBox="0 0 560 897">
    <g stroke="var(--brown)" stroke-width="3">
      <line x1="54" y1="572" x2="110" y2="626"/>
      <line x1="54" y1="584" x2="98" y2="626"/>
      <line x1="54" y1="596" x2="86" y2="626"/>
      <line x1="504" y1="572" x2="448" y2="626"/>
      <line x1="504" y1="584" x2="460" y2="626"/>
      <line x1="504" y1="596" x2="472" y2="626"/>
      <line x1="54" y1="635" x2="504" y2="635"/>
      <line x1="54" y1="643" x2="504" y2="643"/>
    </g>
    <polygon points="259,644 295,644 277,670" fill="var(--brown)"/>
  </svg>

  <p class="abs center relocating">WE'RE RELOCATING TO</p>
  <p class="abs center downtown">DOWNTOWN DUNMORE</p>
  <p class="abs center opening">OPENING NOVEMBER 1<sup>ST</sup></p>

  <div class="abs dot-band" style="left:6px;top:795px;width:548px" role="img" aria-label="Row of light blue dots"></div>

  <footer>
    <p class="abs address">4785 CRESTHAVEN BLVD. DUNMORE, CA 94318</p>
    <p class="abs phone">P: (415) 826-3319</p>
  </footer>
</main>
</body>
</html>
```